Business Card Design

BBQ Concessions and Event Catering
Hi! My name is Dale I am looking for a biz card design for my BBQ company:
We specialize in ribs, brisket, pulled pork, chicken
Mainly Pork Product
Colors: Dark colors, Red, Black
Flames optional
This is a mobile trailer that moves to the party!
Copper Barn is a song by Lonnie Vasquell which influenced the name of my company. So I Love Blues and BBQ!
We also cater at music venues, parties, receptions etc. Anyone who needs good BBQ comes to us.

Looking forward to your designs.

Industry/Entity Type

Business

Contact Information for Business Card

Copper Barn BBQ, Dale Morrow Owner, 2718 Osgood Ave. Millbrook, Oh. 46912

```html
<!DOCTYPE html>
<html lang="en">
<head>
<meta charset="utf-8">
<title>Copper Barn BBQ – Business Card</title>
<link rel="stylesheet" href="https://fonts.googleapis.com/css2?family=Courgette&family=Arimo:wght@400;700&display=swap">
<style>
  :root {
    --backdrop: #d9d9d9;
    --card-white: #ffffff;
    --brand-red: #ec1c24;
    --card-black: #000000;
    --text-light: #ffffff;
  }
  * { margin: 0; padding: 0; box-sizing: border-box; }
  html, body {
    width: 1200px;
    height: 848px;
    overflow: hidden;
    background: var(--backdrop);
  }
  .canvas {
    position: relative;
    width: 1200px;
    height: 848px;
    display: flex;
    align-items: center;
    justify-content: center;
  }
  .business-card {
    position: relative;
    width: 840px;
    height: 480px;
    border-radius: 22px;
    overflow: hidden;
    background: var(--card-black);
    box-shadow: 0 10px 30px rgba(0,0,0,0.25);
  }
  .brand-panel {
    position: absolute;
    left: 0; top: 0;
    width: 100%;
    height: 248px;
    background: var(--card-white);
    display: flex;
    align-items: center;
    justify-content: center;
    padding-top: 40px;
  }
  .brand-name {
    font-family: "Courgette", cursive;
    font-weight: 400;
    font-size: 80px;
    color: var(--brand-red);
    letter-spacing: 1px;
    white-space: nowrap;
  }
  .accent-stripe {
    position: absolute;
    left: 0; top: 248px;
    width: 100%;
    height: 24px;
    background: var(--brand-red);
  }
  .contact-panel {
    position: absolute;
    left: 0; top: 272px;
    width: 100%;
    height: 208px;
    color: var(--text-light);
    font-family: "Arimo", Arial, sans-serif;
    text-align: center;
  }
  .person-name {
    margin-top: 22px;
    font-size: 40px;
    font-weight: 700;
    line-height: 1.05;
  }
  .person-title {
    font-size: 33px;
    font-weight: 400;
    line-height: 1.1;
  }
  .address {
    margin-top: 44px;
    font-size: 27px;
    font-weight: 400;
    white-space: nowrap;
  }
</style>
</head>
<body>
  <main class="canvas">
    <section class="business-card">
      <div class="brand-panel">
        <h1 class="brand-name">Copper Barn BBQ</h1>
      </div>
      <div class="accent-stripe"></div>
      <div class="contact-panel">
        <p class="person-name">Dale Morrow</p>
        <p class="person-title">Owner</p>
        <p class="address">2718 Osgood Ave. Millbrook, Oh. 46912</p>
      </div>
    </section>
  </main>
</body>
</html>
```